Flyer for family counseling

For my family counseling I'm looking for a design for flyers. Important is not only the appearance of the flyer, but also the content design. All important contents can be found on my website: www.helga-brandtner.at The following items should NOT appear on the flyer: - constellation work - bereavement and palliative work My logo should definitely be on the flyer. Source files are available.

Target Market(s)

Families, individuals, children, couples in need of psychological support.

Colors

Designer to choose colors to be used in the design.

Requirements
Must have
• My logo - source files available Website and contact data Recognition value from website to flyer and vice versa
Should not have
• Mention of the constellation work and mourning and palliative work not desired.

```html
<!DOCTYPE html>
<html lang="en">
<head>
<meta charset="utf-8">
<title>Family Counseling Flyer – Front and Back</title>
<link rel="stylesheet" href="https://fonts.googleapis.com/css2?family=Cinzel:wght@500&family=Montserrat:wght@400;500;600;700&family=Roboto+Condensed:wght@400&display=swap">
<style>
:root{
  --teal:#1ba89c;
  --teal-dark:#14897f;
  --blue:#1b72b8;
  --navy:#1d4e86;
  --text:#55595e;
  --footer-grey:#5f6266;
  --backdrop:#e9e8e5;
  --white:#ffffff;
}
*{box-sizing:border-box;margin:0;padding:0}
html,body{width:1200px;height:1200px;overflow:hidden}
body{background:var(--backdrop);font-family:"Montserrat",sans-serif;color:var(--text);position:relative}
.flyer{position:absolute;top:205px;width:558px;height:790px;background:var(--white);overflow:hidden;box-shadow:0 2px 10px rgba(0,0,0,.12)}
.flyer--front{left:26px}
.flyer--back{left:617px}
.abs{position:absolute}

/* hero */
.hero{left:0;top:0;width:558px;height:278px;background:linear-gradient(90deg,#f4f6f8 0%,#eef1f4 40%,#e6eaee 100%)}
.hero-photo{left:196px;top:0;width:362px;height:274px;background:linear-gradient(135deg,#e9e2d8 0%,#d8c2a8 35%,#b38a6a 60%,#4f6e9c 85%,#2e4d7a 100%);border-bottom-left-radius:60px 40px}
.brand{left:20px;top:36px;width:200px;text-align:center}
.brand-mark{width:34px;height:34px;border-radius:50%;background:var(--teal);margin:0 auto 22px}
.brand-name{font-family:"Cinzel",serif;font-weight:500;font-size:9.5px;letter-spacing:.5px;color:var(--teal-dark)}
.brand-tag{font-family:"Cinzel",serif;font-weight:500;font-size:5.6px;letter-spacing:2.6px;color:var(--teal-dark);margin-top:2px}
.headline{left:32px;top:124px;font-family:"Cinzel",serif;font-weight:500;font-size:17px;line-height:20px;color:var(--blue);letter-spacing:.3px}
.hero-checks{left:32px;top:222px;list-style:none;font-family:"Roboto Condensed",sans-serif;font-size:7.6px;line-height:10.5px;color:#4a4d52}
.hero-checks li{padding-left:12px;position:relative}
.hero-wave{left:0;top:256px;width:558px;height:30px}

/* photo cards */
.card{position:absolute;width:228px}
.card-photo{width:228px;height:130px;border-radius:10px 10px 10px 0;border:1px solid #d7dde2}
.card-label{height:18px;width:161px;background:var(--teal);color:var(--white);font-weight:600;font-size:9.4px;letter-spacing:.5px;line-height:18px;padding-left:6px;border-radius:0 0 14px 0;margin-top:-1px}

/* text columns */
.col{position:absolute;width:228px}
.col h3{font-size:9.2px;font-weight:700;color:var(--navy);margin-bottom:7px}
.col p{font-size:6.5px;line-height:8.8px;text-align:justify;margin-bottom:9px}
.lead{font-size:9px!important;line-height:11px!important;font-weight:500;color:var(--navy);text-align:justify}
.ask{list-style:none;margin-bottom:9px}
.ask li{font-size:8.6px;font-weight:500;color:var(--navy);margin-bottom:8.5px;padding-left:11px;position:relative}
.tick-fill::before{content:"";position:absolute;left:0;top:1px;width:8px;height:8px;border-radius:50%;background:var(--teal)}
.tick-fill::after{content:"";position:absolute;left:2.6px;top:2.6px;width:2px;height:3.6px;border:solid var(--white);border-width:0 1.2px 1.2px 0;transform:rotate(40deg)}
.hero-checks li.tick-fill::before{top:1.5px}
.hero-checks li.tick-fill::after{top:3px}
.help{list-style:none}
.help li{font-size:6.6px;line-height:8.8px;padding-left:12px;position:relative;margin-bottom:4.4px}
.tick-ring::before{content:"";position:absolute;left:0;top:.5px;width:6.4px;height:6.4px;border-radius:50%;border:.9px solid var(--teal)}
.tick-ring::after{content:"";position:absolute;left:2.6px;top:1.8px;width:1.6px;height:2.8px;border:solid var(--teal);border-width:0 .9px .9px 0;transform:rotate(40deg)}

/* professional background */
.background-panel{left:0;top:293px;width:261px;height:454px;background:var(--teal);border-radius:0 0 14px 0}
.background-head{left:0;top:293px;width:240px;height:16px;background:var(--blue);color:var(--white);font-weight:600;font-size:8.4px;line-height:16px;padding-left:37px;letter-spacing:.3px}
.portrait{left:198px;top:266px;width:66px;height:66px;border-radius:50%;border:2px solid var(--white);background:radial-gradient(circle at 50% 40%,#f2cfb6 0%,#e7b07d 40%,#d9464a 75%,#e9eef2 100%);box-shadow:0 0 0 1px #9ad3cd}
.timeline{left:34px;top:316px;width:220px;list-style:none;color:var(--white)}
.timeline li{font-size:6.9px;line-height:9.6px;position:relative}
.timeline li b{font-weight:700;display:block}
.timeline li b::before{content:"";position:absolute;left:-7px;top:3.5px;width:2.6px;height:2.6px;border-radius:50%;background:var(--white)}

/* testimonials */
.voices-title{font-size:9.8px;font-weight:700;color:var(--blue);letter-spacing:.4px;margin:0 0 7px}
.quote{position:relative;border:1px solid #4c8fc9;border-left:none;border-top:none;border-radius:0 10px 10px 0;padding:4px 8px 3px 0;margin-bottom:10px;border-right-width:1px}
.quote::before{content:"\201C";position:absolute;left:0;top:-6px;font-size:11px;font-weight:700;color:var(--blue)}
.quote p{font-style:italic;font-size:6.5px;line-height:8.6px;margin-bottom:2px}
.quote cite{display:block;text-align:right;font-style:normal;font-size:7.4px;color:var(--blue);font-weight:500}

/* footer */
.footer{left:0;top:740px;width:558px;height:50px}
.footer-info{left:34px;top:761px;height:22px;line-height:22px;font-size:7.3px;color:var(--white);display:flex;gap:10px;align-items:center}
.footer-info span{display:inline-flex;align-items:center;gap:3px}
.footer-phone{left:404px;top:755px;font-size:11px;font-weight:600;color:var(--white);display:flex;align-items:center;gap:6px}
</style>
</head>
<body>

<!-- FRONT SIDE -->
<section class="flyer flyer--front">
  <div class="abs hero"></div>
  <div class="abs hero-photo" role="img" aria-label="Photo: a counselor with clipboard talking with a smiling couple holding their baby on a sofa"></div>

  <div class="abs brand">
    <div class="brand-mark"></div>
    <div class="brand-name">HELGA BRANDTNER</div>
    <div class="brand-tag">FAMILIENBERATUNG LINDENHOF</div>
  </div>

  <h1 class="abs headline">Has your life<br>reached a point<br>where change<br>is needed?</h1>

  <ul class="abs hero-checks">
    <li class="tick-fill">Accompanying people in their development ...</li>
    <li class="tick-fill">Attention, peace and serenity ...</li>
    <li class="tick-fill">Clear structures and a properly understood<br>approach to discipline ...</li>
  </ul>

  <svg class="abs hero-wave" viewBox="0 0 558 30" preserveAspectRatio="none">
    <path d="M0 20 L300 20 C420 20 520 14 558 0 L558 30 L0 30 Z" fill="#ffffff"/>
    <path d="M0 20 L300 20 C420 20 520 14 558 0" fill="none" stroke="#1ba89c" stroke-width="2"/>
    <path d="M90 26 C300 26 480 22 558 4 L558 10 C480 26 300 28 90 28 Z" fill="#1b72b8"/>
  </svg>

  <div class="card" style="left:33px;top:305px">
    <div class="card-photo" role="img" aria-label="Photo: counselor and client sitting in armchairs in a bright practice room" style="background:linear-gradient(160deg,#f4efe6 0%,#e7ddcc 45%,#8d8f95 70%,#b23a3a 100%)"></div>
    <div class="card-label">INDIVIDUAL COUNSELING</div>
  </div>
  <div class="card" style="left:294px;top:305px">
    <div class="card-photo" role="img" aria-label="Photo: a woman reading a picture book with two girls" style="background:linear-gradient(160deg,#f1f0ea 0%,#d9b98c 40%,#c2723f 65%,#6b2b3a 100%)"></div>
    <div class="card-label">CHILD GUIDANCE</div>
  </div>

  <div class="col" style="left:33px;top:469px">
    <h3>Unauthorized from the crisis</h3>
    <ul class="ask">
      <li class="tick-fill">Is it enough for you?</li>
      <li class="tick-fill">Has a point been reached where nothing works?</li>
      <li class="tick-fill">Is the time ripe for change?</li>
    </ul>
    <p>There are ways out of the impasse. Lots! Enough resources - they just have to be released.</p>
    <p>For the very personal way to self-determination. Once entered, personal development becomes a wonderful adventure.</p>
    <h3 style="margin-top:12px">The individual advice helps:</h3>
    <ul class="help">
      <li class="tick-ring">to regain more joie de vivre</li>
      <li class="tick-ring">yes to say to yourself and to accept it better</li>
      <li class="tick-ring">To change conflict patterns</li>
      <li class="tick-ring">to gain more self-confidence</li>
      <li class="tick-ring">change negative behaviors</li>
      <li class="tick-ring">Make room for yourself and the positive things in life</li>
      <li class="tick-ring">Solve your problems on your own responsibility</li>
      <li class="tick-ring">take a new attitude to yourself and others</li>
      <li class="tick-ring">regain access to your blocked resources</li>
    </ul>
  </div>

  <div class="col" style="left:294px;top:469px">
    <h3>guide - lead - accompany</h3>
    <p class="lead">Court-ordered family, parenting or educational counseling according to § 107 Abs. 3 Z 1 AussStrG</p>
    <p style="margin-top:12px">In the case of non-functioning custody and contact regulations, disagreement between parents about the design of parenting and / or serious problems in parental communication, it is incumbent upon the court to order compulsory educational counseling pursuant to section 107 (3) (1) of the Outcome Tax Act.</p>
    <p>My job is to assist you in a trusting environment, to find a new form of parental cooperation and to focus your attention on the needs and needs of the child / child, develop beneficial attitudes or behaviors to relieve children and their development needs are recognized again.</p>
    <h3 style="margin-top:12px">Out-of-court education advice</h3>
    <p>Children are a wonderful gift. And a big challenge. Sometimes we need help from the outside to meet again lovingly and with mutual respect.</p>
    <p>My most important school is my life and work. In my practice I have learned to deal with very different problems. One result was always the same: there is always a solution. One that makes us sleep soundly again. Regardless of whether we are dealing with behavioral problems or learning disabilities.</p>
  </div>

  <svg class="abs footer" viewBox="0 0 558 50">
    <rect x="0" y="21" width="400" height="22" fill="#5f6266"/>
    <path d="M376 50 C386 50 384 6 404 6 L558 6 L558 50 Z" fill="#ffffff"/>
    <path d="M382 50 C392 50 390 6 410 6 L558 6 L558 50 Z" fill="#1b72b8"/>
  </svg>
  <div class="abs footer-info">
    <span><svg width="8" height="9" viewBox="0 0 8 9"><circle cx="4" cy="3" r="2" fill="none" stroke="#fff" stroke-width="1"/><path d="M1 8.5 C1 6 7 6 7 8.5" fill="none" stroke="#fff" stroke-width="1"/></svg>Lindengasse 14/3, 1070 Vienna</span>
    <span><svg width="9" height="7" viewBox="0 0 9 7"><rect x=".5" y=".5" width="8" height="6" fill="none" stroke="#fff"/><path d="M.5 .5 L4.5 4 L8.5 .5" fill="none" stroke="#fff"/></svg>familienberatung@helga-brandtner.at</span>
  </div>
  <div class="abs footer-phone">
    <svg width="11" height="11" viewBox="0 0 11 11"><path d="M2 1 L4 1 L5 3.5 L3.7 4.5 C4.4 6 5 6.6 6.5 7.3 L7.5 6 L10 7 L10 9 C10 9.6 9.5 10 9 10 C4.5 9.7 1.3 6.5 1 2 C1 1.5 1.4 1 2 1 Z" fill="none" stroke="#fff" stroke-width="1"/></svg>
    +43 660 418 27 95
  </div>
</section>

<!-- BACK SIDE -->
<section class="flyer flyer--back">
  <div class="card" style="left:34px;top:33px">
    <div class="card-photo" role="img" aria-label="Photo: a couple in armchairs talking with the counselor around a small round table" style="background:linear-gradient(160deg,#f5f0e6 0%,#e3d6c0 40%,#4a4c53 70%,#c9b79d 100%)"></div>
    <div class="card-label">COUPLES COUNSELING</div>
  </div>
  <div class="card" style="left:295px;top:33px">
    <div class="card-photo" role="img" aria-label="Photo: parents and two children sitting together with the counselor in the practice room" style="background:linear-gradient(160deg,#f5f0e6 0%,#e0d2ba 40%,#3d4654 68%,#c84646 100%)"></div>
    <div class="card-label">FAMILY &amp; CHILDREN</div>
  </div>

  <div class="col" style="left:34px;top:197px;width:228px">
    <h3>Basis and new beginning</h3>
    <p>Marital or partnership problems - always the same topics or situations, the feeling of being in a circle.</p>
    <p>Patterns can be resolved! I would like to support you on your way to reflect on your partnership in its partnership. To build on, to venture a promising new beginning.</p>
  </div>

  <div class="abs background-panel"></div>
  <div class="abs background-head">PROFESSIONAL BACKGROUND</div>
  <div class="abs portrait" role="img" aria-label="Portrait photo of the counselor"></div>
  <ul class="abs timeline">
    <li><b>December 2017</b>course Deeskalationsmanagement</li>
    <li><b>April 2017</b>Certificate of Recognition as Family, Parenting and Parenting Consultant in accordance with § 107 Abs. 3 Z 1 AussStrG</li>
    <li><b>November 2015</b>Education: MOVE - motivational short intervention in (risky) consuming adolescents</li>
    <li><b>October 2015</b>Training: Hypnosystemic mourning for severe and complicated mourning</li>
    <li><b>May 2015</b>Training: Hypnotherapy for anxiety disorders</li>
    <li><b>January 2015</b>Course: Life, death and grief counseling</li>
    <li><b>October 2014</b>Interdisciplinary Symposium: Couples in Motion</li>
    <li><b>November 2013</b>Training: feelings of guilt and powerlessness</li>
    <li><b>October 2013</b>Qualification recognition for the counseling of parents according to § 95 Abs. 1a AussStrG about the specific needs of their minor children resulting from the divorce</li>
    <li><b>June 2013</b>Seminar: Nonviolent Communication after Martin K. Rosswald</li>
    <li><b>November 2011</b>Diploma in Systemic Installation Management</li>
    <li><b>October 2010</b>Training: Experience-oriented developmental psychology</li>
    <li><b>May 2009</b>Training: Developmental psychology for children from 3 to 6 years</li>
    <li><b>April 2008</b>Training: psychodiagnostics and general psychology</li>
    <li><b>October 2007</b>Training: Conflict Psychology and Methodology</li>
    <li><b>June 2007</b>Education: Systemic life and social counselor</li>
    <li><b>June 2006</b>Education: Systemic Coaching</li>
  </ul>

  <div class="col" style="left:295px;top:197px;width:228px">
    <h3>Living together</h3>
    <h3 style="margin-top:-1px">What is a family counseling and how does it work?</h3>
    <p>By this I mean a session in which every single member of the family is given space and space to express their concerns, wishes and needs under professional guidance. In the attitude that the competence to solve the problem lies within the family itself, the strengths and resources of the family are exposed in order to achieve a positive relationship change between the individual family members. I accompany this process with all-party appreciative leadership.</p>
    <p>Family counseling can also be useful for individuals.</p>
    <p>After the goal first defined jointly by the family, the focus is put on the strengths and resources of the family, because as a consultant I assume that the competence to solve the problem always lies within the family itself and requires only professional, appreciative support.</p>
    <h3 style="margin-top:10px">Themes of a family counseling</h3>
    <p>Children are a wonderful gift. And a big challenge. Sometimes we need help from the outside to meet again lovingly and with mutual respect.</p>
    <p>My most important school is my life and work. In my practice I have learned to deal with very different problems. One result was always the same: there is always a solution. One that makes us sleep soundly again. Regardless of whether we are dealing with behavioral problems or learning disabilities.</p>
    <h3 style="margin-top:10px">The individual advice helps:</h3>
    <ul class="help">
      <li class="tick-ring">child guidance</li>
      <li class="tick-ring">Life crises, such as a death or serious life events (eg: burn out, accidents, ...)</li>
      <li class="tick-ring">Pronounced or unspoken conflicts within the family, with the result that there are communication difficulties</li>
      <li class="tick-ring">Behavioral problems of a child at school due to ADHD, school refusal, bullying, adolescent crises, Internet, mobile phone and computer addiction, examination anxiety, and much more.</li>
    </ul>
  </div>

  <div class="col" style="left:295px;top:625px;width:228px">
    <div class="voices-title">VOICES OF CLIENTS :</div>
    <div class="quote">
      <p>Helga Brandtner is characterized by warmth, sovereignty, calm and care. Safe and loving, she accompanies you through the process. She is neutral, but interested. You feel well cared for, even if it is "taken care of".</p>
      <cite>Mrs. R. client »</cite>
    </div>
    <div class="quote">
      <p>My way was full of stones and wood. I took the broom in the hand and returned. Mrs. Brandtner accompanied me.</p>
      <cite>Mrs. H. client »</cite>
    </div>
  </div>

  <svg class="abs footer" viewBox="0 0 558 50">
    <rect x="0" y="21" width="400" height="22" fill="#5f6266"/>
    <path d="M376 50 C386 50 384 6 404 6 L558 6 L558 50 Z" fill="#ffffff"/>
    <path d="M382 50 C392 50 390 6 410 6 L558 6 L558 50 Z" fill="#1b72b8"/>
  </svg>
  <div class="abs footer-info">
    <span><svg width="8" height="9" viewBox="0 0 8 9"><circle cx="4" cy="3" r="2" fill="none" stroke="#fff" stroke-width="1"/><path d="M1 8.5 C1 6 7 6 7 8.5" fill="none" stroke="#fff" stroke-width="1"/></svg>Lindengasse 14/3, 1070 Vienna</span>
    <span><svg width="9" height="7" viewBox="0 0 9 7"><rect x=".5" y=".5" width="8" height="6" fill="none" stroke="#fff"/><path d="M.5 .5 L4.5 4 L8.5 .5" fill="none" stroke="#fff"/></svg>familienberatung@helga-brandtner.at</span>
  </div>
  <div class="abs footer-phone">
    <svg width="11" height="11" viewBox="0 0 11 11"><path d="M2 1 L4 1 L5 3.5 L3.7 4.5 C4.4 6 5 6.6 6.5 7.3 L7.5 6 L10 7 L10 9 C10 9.6 9.5 10 9 10 C4.5 9.7 1.3 6.5 1 2 C1 1.5 1.4 1 2 1 Z" fill="none" stroke="#fff" stroke-width="1"/></svg>
    +43 660 418 27 95
  </div>
</section>

</body>
</html>
```